Velmorak720 is a marketing advisory service company. We provide the following services:
Marketing Strategy
PR and Marketing Communication
Field Marketing
Digital Marketing

We would like to see a design that has either of the following copy:

Everyone can develop a product for the market; not everyone can access the market with the product. Let Velmorak720 help you access the market profitably.

or

Almost every business know how to create value, nor every business can capture value. At Velmorak720, we specialize in helping businesses capture value.

or

It is easy to start a business, attracting and retaining customers and client is the real work. At Velmorak720, we specialize in helping our businesses attract and retain customers and clients.

We can have a slogan that reads:

V-720, your market development partner.....

```html
<!DOCTYPE html>
<html lang="en">
<head>
<meta charset="utf-8">
<title>Velmorak720 – Web Banner Set</title>
<link rel="stylesheet" href="https://fonts.googleapis.com/css2?family=Arimo:wght@400;700&family=Tinos:wght@400;700&family=Open+Sans:wght@600&family=Roboto+Condensed:wght@400&display=swap">
<style>
  :root {
    --board-light: #f2f2f2;
    --board-mid: #9a9a9a;
    --board-dark: #3a3a3a;
    --banner-top: #1d5d84;
    --banner-mid: #164b6e;
    --banner-deep: #0c2f48;
    --text-white: #ffffff;
    --highlight: #f2e21a;
    --cta: #f05a12;
    --cta-light: #ff7a2e;
    --logo-blue: #1c3f94;
    --caption: #ffffff;
  }
  * { box-sizing: border-box; margin: 0; padding: 0; }
  html, body { width: 1200px; height: 928px; overflow: hidden; }
  body {
    position: relative;
    background:
      radial-gradient(ellipse 760px 520px at 380px 380px, var(--board-light) 0%, #cfcfcf 35%, var(--board-mid) 70%, var(--board-dark) 100%);
    font-family: "Arimo", Arial, sans-serif;
  }
  .board-swoosh { position: absolute; inset: 0; width: 1200px; height: 928px; }

  .banner {
    position: absolute;
    width: 440px;
    height: 372px;
    background: linear-gradient(180deg, var(--banner-top) 0%, var(--banner-mid) 45%, var(--banner-deep) 100%);
    box-shadow: 6px 8px 14px rgba(0,0,0,0.55);
    overflow: hidden;
  }
  .banner--access { left: 90px; top: 44px; }
  .banner--value { left: 630px; top: 44px; }
  .banner--retain { left: 364px; top: 434px; }

  .brand-box {
    position: absolute;
    left: 8px; top: 8px;
    width: 124px; height: 126px;
    background: var(--text-white);
    display: flex; flex-direction: column; align-items: center; justify-content: center;
    gap: 12px;
  }
  .brand-mark { width: 46px; height: 46px; background: var(--logo-blue); }
  .brand-name {
    font-family: "Arimo", Arial, sans-serif;
    font-weight: 700;
    font-size: 17px;
    color: var(--logo-blue);
  }

  .slogan {
    position: absolute;
    left: 150px; top: 26px;
    width: 280px;
    font-family: "Tinos", "Times New Roman", serif;
    color: var(--text-white);
    font-size: 24px;
    line-height: 1.15;
    text-align: center;
  }
  .slogan-code { font-size: 36px; font-weight: 700; }

  .pitch {
    position: absolute;
    left: 22px; top: 150px;
    width: 400px;
    font-size: 22.5px;
    line-height: 1.2;
    color: var(--text-white);
  }
  .banner--access .pitch { text-align: center; }
  .pitch .hl { color: var(--highlight); }

  .art {
    position: absolute;
    left: 0; bottom: 0;
    width: 170px; height: 120px;
  }
  .art--access { background: radial-gradient(circle at 45% 60%, #8fb2d2 0%, #4a7aa6 45%, rgba(30,80,120,0) 75%); }
  .art--value { width: 180px; height: 130px; background: linear-gradient(160deg, rgba(200,190,90,0.0) 10%, #a8a35a 45%, #5d6a3a 100%); }
  .art--retain { width: 160px; height: 96px; background: radial-gradient(ellipse at 40% 55%, #dfe8f0 0%, #9db7cf 45%, rgba(40,90,130,0) 78%); }

  .cta {
    position: absolute;
    right: 42px; bottom: 22px;
    width: 196px; height: 52px;
    border-radius: 6px;
    background: linear-gradient(180deg, var(--cta-light) 0%, var(--cta) 60%, #d84a08 100%);
    color: var(--text-white);
    font-family: "Open Sans", Arial, sans-serif;
    font-weight: 600;
    font-size: 23px;
    display: flex; align-items: center; justify-content: center;
  }
  .banner--value .cta { bottom: 32px; }

  .board-caption {
    position: absolute;
    left: 256px; top: 864px;
    width: 640px;
    font-family: "Roboto Condensed", "Arial Narrow", sans-serif;
    font-size: 14px;
    line-height: 1.3;
    color: var(--caption);
  }
</style>
</head>
<body>
  <svg class="board-swoosh" viewBox="0 0 1200 928" aria-hidden="true">
    <path d="M0 470 C 300 700, 760 760, 1200 640 L1200 928 L0 928 Z" fill="#4a4a4a" opacity="0.55"/>
    <path d="M0 470 C 300 700, 760 760, 1200 640" fill="none" stroke="#d8d8d8" stroke-width="2" opacity="0.5"/>
  </svg>

  <section class="banner banner--access">
    <div class="brand-box"><span class="brand-mark"></span><span class="brand-name">Velmorak720</span></div>
    <h2 class="slogan"><span class="slogan-code">V-720</span> Your Market Development Partner</h2>
    <p class="pitch"><span class="hl">Everyone</span> can develop a product for the market; <span class="hl">Not everyone</span> can access the market with the product. <span class="hl">Let Velmorak720</span> help you access the market profitably.</p>
    <div class="art art--access" role="img" aria-label="Illustration of a person at a laptop in front of a gear"></div>
    <a class="cta">Learn more</a>
  </section>

  <section class="banner banner--value">
    <div class="brand-box"><span class="brand-mark"></span><span class="brand-name">Velmorak720</span></div>
    <h2 class="slogan"><span class="slogan-code">V-720</span> Your Market Development Partner</h2>
    <p class="pitch"><span class="hl">Almost</span> every business know how to create value, <span class="hl">Nor</span> every business can capture value. At <span class="hl">Velmorak720</span> we specializein <span class="hl">helping business</span> capture value.</p>
    <div class="art art--value" role="img" aria-label="Yellow road sign reading core values"></div>
    <a class="cta">Learn more</a>
  </section>

  <section class="banner banner--retain">
    <div class="brand-box"><span class="brand-mark"></span><span class="brand-name">Velmorak720</span></div>
    <h2 class="slogan"><span class="slogan-code">V-720</span> Your Market Development Partner</h2>
    <p class="pitch">It is <span class="hl">easy to start</span> a business, attracting and retaining customer and client is the real work. <span class="hl">At Velmorak720</span> we <span class="hl">specialize</span> in helping our <span class="hl">business</span> attract and retain customers and clients.</p>
    <div class="art art--retain" role="img" aria-label="Magnifying glass over the word expert"></div>
    <a class="cta">Learn more</a>
  </section>

  <p class="board-caption">This is Pixelforge's version of Lorem Ipsum. Proin gravida nibh vel velit auctor aliquet. Aenean sollicitudin, lorem quis bibendum auctor, nisi elit consequat ipsum, nec sagittis sem nibh id elit. Duis sed odio sit amet nibh vulputate cursus a sit amet mauris. Morbi accumsan ipsum velit. Nam</p>
</body>
</html>
```